Business card for biotech sales agent

I need a logo and business card designed for my company Telmora. We work in partnership with Kivex Group. Kivex have developed advanced biotech. Their hand sanitiser is alcohol free and works for 24 hours on skin, even with regular hand washing. The surface sanitiser works for up to 30 days on surfaces and fabrics. Its food-safe, it's non-toxic, safe for animals and humans. The products have a very wide variety of applications: everything from agri-business, hotels, hospitality, schools, child and baby care, transport, meat processing etc.<br/>I would like my design to use blues or green-blues and communicate a bit of nano-tech but also trust and safety.<br/>I would also use the Kivex logo on my card next to 'sales & distribution agent'

Target Market(s)

B2B, selling to FMCG and large companies such as airlines

Industry/Entity Type

Biotechnology

Contact Information for Business Card

Joan Pelling
Director

Phone: +64 22 519 3064
Email: joan@telmora.co
www.telmora.co
14 Callery St, Westhaven, Auckland, New Zealand 1047

Font styles to use
Sans Serif

Colors
3276b5
33b8a4
34a7d8
3176b5
ffffff

Requirements
Must have
• Not be too busy, clean space is good
• A logo styling to the word Telmora
Nice to have
• A little bit of a bio-tech image as a screen perhaps

```html
<!DOCTYPE html>
<html lang="en">
<head>
<meta charset="utf-8">
<title>Telmora Agency — Business Card</title>
<link href="https://fonts.googleapis.com/css2?family=Open+Sans:wght@400;600;700&display=swap" rel="stylesheet">
<style>
  :root {
    --brand-blue: #3176b5;
    --brand-teal: #33b8a4;
    --sky: #34a7d8;
    --white: #ffffff;
    --ink: #1a1a1a;
    --backdrop: #e6e8eb;
  }
  * { box-sizing: border-box; margin: 0; padding: 0; }
  html, body { width: 1200px; height: 1021px; overflow: hidden; }
  body {
    background: var(--backdrop);
    font-family: "Open Sans", Arial, sans-serif;
    display: flex;
    flex-direction: column;
    align-items: center;
    justify-content: center;
    gap: 22px;
  }
  .card {
    width: 840px;
    height: 480px;
    position: relative;
    overflow: hidden;
    box-shadow: 0 6px 18px rgba(0,0,0,.18);
  }

  /* Shared brand lockup */
  .brand { display: flex; align-items: center; gap: 18px; color: var(--white); font-weight: 600; }
  .brand-dot { width: 60px; height: 60px; border-radius: 50%; background: var(--brand-teal); flex: none; }
  .brand-name { display: flex; flex-direction: column; line-height: 1; }
  .brand-name .word { font-size: 100px; letter-spacing: -1px; line-height: 0.9; }
  .brand-name .sub { font-size: 24px; font-weight: 400; letter-spacing: 18px; align-self: flex-end; margin-top: 18px; margin-right: -18px; }

  /* Front */
  .card-front { background: var(--brand-blue); display: flex; align-items: center; justify-content: center; }

  /* Back */
  .card-back { background: var(--white); }
  .brand-vertical {
    position: absolute;
    left: 112px; top: 240px;
    transform: translate(-50%, -50%) rotate(-90deg);
    color: var(--brand-blue);
    gap: 12px;
  }
  .brand-vertical .brand-dot { width: 38px; height: 38px; }
  .brand-vertical .word { font-size: 60px; }
  .brand-vertical .sub { font-size: 15px; letter-spacing: 10px; margin-top: 12px; margin-right: -10px; }
  .divider { position: absolute; left: 212px; top: 100px; width: 3px; height: 280px; background: var(--brand-blue); }
  .contact-block { position: absolute; left: 258px; top: 120px; }
  .person { font-size: 32px; font-weight: 700; letter-spacing: 2px; color: var(--ink); line-height: 1.1; }
  .person .surname { color: var(--brand-blue); }
  .role { font-size: 19px; color: var(--ink); letter-spacing: 1px; margin-bottom: 26px; }
  .contact-list { list-style: none; }
  .contact-list li { display: flex; align-items: flex-start; gap: 16px; font-size: 21px; letter-spacing: 1.5px; color: var(--ink); line-height: 1.35; margin-bottom: 6px; }
  .contact-list svg { width: 20px; height: 20px; flex: none; margin-top: 5px; fill: var(--brand-blue); }
</style>
</head>
<body>

  <section class="card card-front" aria-label="Card front">
    <div class="brand">
      <span class="brand-dot"></span>
      <span class="brand-name"><span class="word">telmora</span><span class="sub">AGENCY</span></span>
    </div>
  </section>

  <section class="card card-back" aria-label="Card back">
    <div class="brand brand-vertical">
      <span class="brand-dot"></span>
      <span class="brand-name"><span class="word">telmora</span><span class="sub">AGENCY</span></span>
    </div>
    <div class="divider"></div>
    <div class="contact-block">
      <p class="person">Joan <span class="surname">Pelling</span></p>
      <p class="role">Director</p>
      <ul class="contact-list">
        <li><svg viewBox="0 0 24 24"><path d="M6.6 10.8a15 15 0 0 0 6.6 6.6l2.2-2.2c.3-.3.7-.4 1-.2 1.1.4 2.3.6 3.6.6.6 0 1 .4 1 1V20c0 .6-.4 1-1 1A17 17 0 0 1 3 4c0-.6.4-1 1-1h3.5c.6 0 1 .4 1 1 0 1.3.2 2.5.6 3.6.1.3 0 .7-.2 1z"/></svg>+64 22 519 3064</li>
        <li><svg viewBox="0 0 24 24"><path d="M2 5h20v14H2zm2 2v.5l8 5 8-5V7l-8 5z"/></svg>joan@telmora.co</li>
        <li><svg viewBox="0 0 24 24"><path d="M12 2a10 10 0 1 0 0 20 10 10 0 0 0 0-20zm6.9 6h-3a15 15 0 0 0-1.3-3.9A8 8 0 0 1 18.9 8zM12 4c.8 1.2 1.5 2.5 1.9 4h-3.8c.4-1.5 1.1-2.8 1.9-4zM4.3 14a8 8 0 0 1 0-4h3.4a16 16 0 0 0 0 4zm.8 2h3a15 15 0 0 0 1.3 3.9A8 8 0 0 1 5.1 16zm3-8h-3a8 8 0 0 1 4.3-3.9C8.8 5.3 8.4 6.6 8.1 8zM12 20c-.8-1.2-1.5-2.5-1.9-4h3.8c-.4 1.5-1.1 2.8-1.900 4zm2.3-6H9.7a14 14 0 0 1 0-4h4.6a14 14 0 0 1 0 4zm.3 5.9c.6-1.2 1-2.5 1.3-3.9h3a8 8 0 0 1-4.3 3.9zm1.7-5.9a16 16 0 0 0 0-4h3.4a8 8 0 0 1 0 4z"/></svg>www.telmora.co</li>
        <li><svg viewBox="0 0 24 24"><path d="M12 2a7 7 0 0 0-7 7c0 5.2 7 13 7 13s7-7.8 7-13a7 7 0 0 0-7-7zm0 9.5a2.5 2.5 0 1 1 0-5 2.5 2.5 0 0 1 0 5z"/></svg><span>14 Callery St, Westhaven,<br>Auckland, New Zealand 1047</span></li>
      </ul>
    </div>
  </section>

</body>
</html>
```